Criação de Peça Gráfica (unidade) para Beleza
A empresa queria:
" Trata-se de um salão de beleza diferenciado, com atendimento VIP e serviços altamente customizados, para atender 100% da demanda do cliente. "

```html
<!DOCTYPE html>
<html lang="pt-BR">
<head>
<meta charset="UTF-8">
<title>Lumé Beauty Center – Moldura para fotos</title>
<link href="https://fonts.googleapis.com/css2?family=Montserrat:wght@400;600&display=swap" rel="stylesheet">
<style>
  :root {
    --bg: #ffffff;
    --ink: #2b2b2b;
    --silver-light: #f2f2f3;
    --silver-mid: #c9cacc;
    --silver-dark: #9c9ea1;
    --icon: #8e9093;
    --mirror-edge: #8f9296;
    --mirror-1: #eef3f5;
    --mirror-2: #a9c8d2;
    --mirror-3: #e3ecef;
  }
  * { margin: 0; padding: 0; box-sizing: border-box; }
  html, body { width: 1200px; height: 1200px; overflow: hidden; background: var(--bg); }
  body { font-family: "Montserrat", sans-serif; position: relative; }

  .brand-panel {
    position: absolute; left: 235px; top: 24px; width: 730px; height: 125px;
    background: var(--bg);
    border: 2px solid var(--silver-mid);
    display: flex; align-items: center; justify-content: center;
  }
  .brand-name { font-size: 46px; font-weight: 600; line-height: 1; color: var(--ink); }

  .frame {
    position: absolute; left: 240px; top: 149px; width: 720px; height: 1016px;
    background: linear-gradient(120deg, var(--silver-light) 0%, var(--silver-mid) 30%, var(--silver-light) 55%, var(--silver-dark) 80%, var(--silver-mid) 100%);
    box-shadow: 0 4px 10px rgba(0,0,0,0.15);
  }

  .post-header { position: absolute; left: 0; top: 38px; width: 100%; height: 68px; }
  .avatar {
    position: absolute; left: 69px; top: 0; width: 68px; height: 68px; border-radius: 50%;
    background: var(--bg); border: 3px solid var(--silver-dark);
  }
  .handle {
    position: absolute; left: 151px; top: 16px; font-size: 31px; font-weight: 600; color: var(--ink);
  }
  .header-bar {
    position: absolute; left: 456px; top: 12px; width: 168px; height: 46px; border-radius: 8px;
    background: linear-gradient(180deg, var(--silver-light), var(--silver-dark));
    border: 4px solid var(--silver-dark);
  }
  .more { position: absolute; left: 640px; top: 28px; }

  .mirror {
    position: absolute; left: 43px; top: 129px; width: 634px; height: 615px;
    border: 10px solid var(--mirror-edge);
    background: linear-gradient(135deg, var(--mirror-1) 0%, var(--mirror-2) 35%, var(--mirror-3) 50%, var(--mirror-2) 70%, var(--mirror-1) 100%);
  }

  .actions { position: absolute; left: 0; top: 774px; width: 100%; height: 44px; }
  .actions svg { position: absolute; top: 0; }

  .likes {
    position: absolute; left: 79px; top: 852px; font-size: 22px; color: var(--ink);
    display: flex; align-items: center; gap: 10px;
  }
  .caption {
    position: absolute; left: 79px; top: 898px; font-size: 24px; color: var(--ink);
    word-spacing: 2px;
  }
  .caption .tag { margin-left: 60px; }
</style>
</head>
<body>
  <header class="brand-panel">
    <div class="brand-name">Lumé Beauty Center</div>
  </header>

  <main class="frame">
    <div class="post-header">
      <div class="avatar"></div>
      <div class="handle">#lumebcenter</div>
      <div class="header-bar"></div>
      <svg class="more" width="30" height="10" viewBox="0 0 30 10">
        <circle cx="5" cy="5" r="3.5" fill="var(--ink)"/>
        <circle cx="15" cy="5" r="3.5" fill="var(--ink)"/>
        <circle cx="25" cy="5" r="3.5" fill="var(--ink)"/>
      </svg>
    </div>

    <div class="mirror" role="img" aria-label="Área espelhada para a foto do cliente"></div>

    <div class="actions">
      <svg style="left:76px" width="42" height="40" viewBox="0 0 42 40">
        <path d="M21 37 C8 27 2 20 2 12 C2 6 7 2 12 2 C16 2 19 4 21 8 C23 4 26 2 30 2 C35 2 40 6 40 12 C40 20 34 27 21 37Z" fill="var(--silver-light)" stroke="var(--icon)" stroke-width="3"/>
      </svg>
      <svg style="left:152px" width="42" height="42" viewBox="0 0 42 42">
        <path d="M21 3 A18 18 0 1 0 36 31 L39 39 L30 35 A18 18 0 0 0 21 3Z" fill="var(--silver-light)" stroke="var(--icon)" stroke-width="3"/>
      </svg>
      <svg style="left:236px" width="44" height="40" viewBox="0 0 44 40">
        <path d="M3 4 L41 4 L22 37 L18 19 Z M18 19 L41 4" fill="var(--silver-light)" stroke="var(--icon)" stroke-width="3" stroke-linejoin="round"/>
      </svg>
      <svg style="left:624px" width="28" height="40" viewBox="0 0 28 40">
        <path d="M3 3 L25 3 L25 37 L14 28 L3 37 Z" fill="var(--silver-light)" stroke="var(--icon)" stroke-width="3" stroke-linejoin="round"/>
      </svg>
    </div>

    <div class="likes">
      <svg width="24" height="22" viewBox="0 0 42 40">
        <path d="M21 37 C8 27 2 20 2 12 C2 6 7 2 12 2 C16 2 19 4 21 8 C23 4 26 2 30 2 C35 2 40 6 40 12 C40 20 34 27 21 37Z" fill="var(--ink)"/>
      </svg>
      <span>362 likes</span>
    </div>
    <p class="caption">Que tal meu look novo?<span class="tag">#lumebcenter</span></p>
  </main>
</body>
</html>
```